Gutschein Design Weihnachtsaktion Mähroboter
Zielgruppe
Installation für Mähroboter
Aufgabenstellung
Format DIN Lang (99x120mm) quer
Gutschein zur Installation eines Mähroboters
Auswahlfelder: für oberirdische oder unterirdische Verlegung
Auswahlfelder: bis 250m²; bis 500m², bis 1.000m²
Adressfeld/Namensfeld für den beschenkten
Serienfeld für Gutscheinnummer
Datums und Unterschriftsfeld
Design Vorstellung: Ein Männchen welches einen Mähroboter installiert, Design Mähroboter mit Weihnachtsmütze.... / Weihnachtliche Grundgestaltung. Sind für Ideen offen!
unser Logo integrieren

```html
<!DOCTYPE html>
<html lang="de">
<head>
<meta charset="utf-8">
<title>Gutschein Mähroboter-Installation</title>
<link rel="stylesheet" href="https://fonts.googleapis.com/css2?family=Great+Vibes&family=Alegreya:wght@400;500&family=Alegreya+Sans:wght@400;500&display=swap">
<style>
  :root{
    --page:#ffffff;
    --wine-dark:#3a0208;
    --wine:#6e0611;
    --wine-light:#8c0d1a;
    --gold:#c9a23c;
    --gold-light:#e8cf7c;
    --gold-text:#c19a3d;
    --field-fill:#fdebb3;
    --circle-fill:#fde9b0;
    --label:#c8a254;
  }
  *{box-sizing:border-box;margin:0;padding:0}
  html,body{width:1167px;height:1200px;overflow:hidden;background:var(--page)}
  body{position:relative;font-family:"Alegreya",serif}

  .card{position:absolute;left:149px;width:869px;height:409px;overflow:hidden;
        box-shadow:0 4px 10px rgba(0,0,0,.35)}
  .card--front{top:130px;
    background:radial-gradient(ellipse at 75% 35%, var(--wine-light) 0%, var(--wine) 45%, var(--wine-dark) 100%)}
  .card--back{top:657px;background:var(--page)}

  .corner{position:absolute;width:140px;height:140px}
  .corner--tl{left:0;top:0}
  .corner--br{right:0;bottom:0}

  .title{position:absolute;left:41px;top:58px;font-family:"Great Vibes",cursive;font-weight:400;
    font-size:166px;line-height:1;white-space:nowrap;color:var(--gold);
    background:linear-gradient(180deg,var(--gold-light),var(--gold) 55%,#9c7622);
    -webkit-background-clip:text;background-clip:text;-webkit-text-fill-color:transparent}
  .subtitle{position:absolute;left:156px;top:232px;font-family:"Alegreya Sans",sans-serif;
    font-size:23px;font-weight:500;line-height:28px;color:var(--gold-light);white-space:nowrap}

  .mower-art{position:absolute;left:597px;top:168px;width:228px;height:198px;border-radius:40% 40% 30% 30%;
    background:radial-gradient(ellipse at 40% 30%, #f2f2f2 0%, #a9a9a9 55%, #5b5b5b 100%)}

  .brand{position:absolute;right:12px;bottom:12px;display:flex;align-items:center;gap:5px;
    font-family:"Alegreya Sans",sans-serif;font-size:14px;font-weight:500;color:var(--wine-light)}
  .brand-dot{width:10px;height:10px;border-radius:50%;background:var(--wine-light)}

  .choose{position:absolute;left:188px;top:32px;font-size:23px;line-height:28px;color:var(--gold-text);white-space:nowrap}
  .option{position:absolute;display:flex;align-items:center;gap:12px;height:28px;
    font-size:21px;line-height:28px;color:var(--gold-text);white-space:nowrap}
  .option .tick{flex:none;width:26px;height:26px;border-radius:50%;background:var(--circle-fill);border:1.5px solid var(--gold)}
  .option--a1{left:187px;top:72px}
  .option--a2{left:187px;top:110px}
  .option--b1{left:559px;top:72px}
  .option--b2{left:559px;top:110px}
  .option--b3{left:559px;top:148px}

  .line-field{position:absolute;left:49px;width:352px;border-top:2px solid var(--gold)}
  .line-field span,.serial-label{display:block;font-family:"Alegreya Sans",sans-serif;font-size:14px;line-height:18px;color:var(--label);padding:4px 0 0 8px;white-space:nowrap}
  .line-field--wide{width:661px}
  .serial-box{position:absolute;left:448px;top:251px;width:261px;height:47px;background:var(--field-fill);border:2px solid var(--gold)}
  .serial-label{position:absolute;left:448px;top:304px}
</style>
</head>
<body>

<section class="card card--front">
  <svg class="corner corner--tl" viewBox="0 0 140 140">
    <defs><linearGradient id="goldBand" x1="0" y1="0" x2="1" y2="1">
      <stop offset="0" stop-color="#8a6420"/><stop offset=".5" stop-color="#f4dc8a"/><stop offset="1" stop-color="#9c7424"/>
    </linearGradient></defs>
    <polygon points="0,0 125,0 0,125" fill="#fff"/>
    <polygon points="118,0 131,0 0,131 0,118" fill="url(#goldBand)"/>
  </svg>
  <h1 class="title">Gutschein</h1>
  <p class="subtitle">zur Installation eines Mähroboters</p>
  <div class="mower-art" role="img" aria-label="Mähroboter in Silbergrau mit roter Weihnachtsmütze"></div>
  <svg class="corner corner--br" viewBox="0 0 140 140">
    <polygon points="140,15 140,140 15,140" fill="#fff"/>
    <polygon points="140,9 140,22 22,140 9,140" fill="url(#goldBand)"/>
  </svg>
  <div class="brand"><span class="brand-dot"></span>Rasenwerk</div>
</section>

<section class="card card--back">
  <svg class="corner corner--tl" viewBox="0 0 140 140">
    <polygon points="118,0 131,0 0,131 0,118" fill="url(#goldBand)"/>
  </svg>

  <p class="choose">Bitte wählen Sie:</p>
  <label class="option option--a1"><span class="tick"></span>oberirdische Verlegung</label>
  <label class="option option--a2"><span class="tick"></span>unterirdische Verlegung</label>
  <label class="option option--b1"><span class="tick"></span>bis 250m²</label>
  <label class="option option--b2"><span class="tick"></span>bis 500m²</label>
  <label class="option option--b3"><span class="tick"></span>bis 1.000m²</label>

  <div class="line-field" style="top:205px"><span>Vor- und Nachname</span></div>
  <div class="line-field" style="top:252px"><span>Straße und Hausnummer</span></div>
  <div class="line-field" style="top:299px"><span>PLZ und Wohnort</span></div>
  <div class="serial-box"></div>
  <span class="serial-label">Gutscheinnummer</span>
  <div class="line-field line-field--wide" style="top:365px"><span>Datum, Unterschrift</span></div>

  <svg class="corner corner--br" viewBox="0 0 140 140">
    <polygon points="140,9 140,22 22,140 9,140" fill="url(#goldBand)"/>
  </svg>
  <div class="brand"><span class="brand-dot"></span>Rasenwerk</div>
</section>

</body>
</html>
```